Brightpath Medical Exercise, LLC specializes in post rehab medical exercise for clients who have been discharged from physical therapy and/or other medical services and are in need of continued cardiovascular, strength, flexibility, endurance training and management of their medical conditions. We strive to bridge the gap between healthcare and fitness by staying in communication with the referring physician and /or physical therapist with updated progress notes to follow each clients progression, making sure each client is appropriate for exercise and identifying any red flags throughout the initial assessment and screening of the client, and referring those clients back to the physician and/or therapist when necessary.
Colors
Designer to choose colors to be used in the design.
Requirements
Must have
- Pictures of a trainer working with a client one on one during exercise, and group exercise
Nice to have
- Pictures that portray the bridge between healthcare and fitness
Should not have
- Cursive writing

```html
<!DOCTYPE html>
<html lang="en">
<head>
<meta charset="utf-8">
<title>Brightpath Medical Exercise – Rack Card</title>
<link href="https://fonts.googleapis.com/css2?family=Black+Ops+One&family=Questrial&family=Lato:ital,wght@0,400;0,700;1,400&display=swap" rel="stylesheet">
<style>
  :root{
    --bg:#636363;
    --card:#ffffff;
    --red:#ef5350;
    --ink:#222325;
    --dark:#2a2b2d;
    --grey-bar:#6b6b6b;
    --list-bg:#f1f1f1;
    --photo-a:#3b4a3a;
    --photo-b:#b59b7e;
  }
  *{box-sizing:border-box;margin:0;padding:0}
  html,body{width:1200px;height:1200px;overflow:hidden;background:var(--bg)}
  .rack-card{position:absolute;top:195px;width:379px;height:825px;background:var(--card);overflow:hidden;font-family:"Lato",sans-serif;color:var(--ink)}
  .rack-card--front{left:142px}
  .rack-card--back{left:618px}

  .brand-mark{position:absolute;left:0;right:0;text-align:center}
  .brand-mark--front{top:45px}
  .brand-mark--back{top:60px}
  .brand-mark__dot{width:80px;height:80px;border-radius:50%;border:4px solid var(--red);margin:0 auto 12px}
  .brand-mark__name{font-family:"Lato",sans-serif;font-weight:700;font-size:9px;line-height:11px;color:var(--ink);letter-spacing:.3px}

  .hero{position:absolute;left:0;top:0;width:379px;height:500px}
  .hero__rings{position:absolute;left:0;top:0}
  .hero__photo{position:absolute;left:52px;top:174px;width:278px;height:308px;border-radius:50%;background:radial-gradient(ellipse at 50% 30%,var(--photo-a) 0%,#5d5a4c 45%,var(--photo-b) 75%,#d8c3a7 100%);border:2px solid #fff}

  .title{position:absolute;left:0;right:0;top:504px;text-align:center;font-family:"Black Ops One",sans-serif;font-weight:400;font-size:23px;line-height:33px;color:var(--ink);letter-spacing:.3px}
  .tagline{position:absolute;left:0;right:0;top:574px;text-align:center;font-family:"Questrial",sans-serif;font-size:15px;line-height:18px;letter-spacing:.4px}
  .label{position:absolute;left:84px;top:628px;width:210px;height:19px;background:var(--red);color:#fff;font-family:"Black Ops One",sans-serif;font-size:11px;line-height:19px;text-align:center;letter-spacing:.2px}
  .services{position:absolute;left:34px;top:656px;width:330px;list-style:none;font-size:14.5px;line-height:18px}
  .services li{position:relative;padding-left:15px;margin-bottom:4px}
  .services li::before,.conditions li::before{content:"";position:absolute;left:0;top:8px;width:4px;height:4px;border-radius:50%;background:var(--red)}

  .footer{position:absolute;left:0;bottom:0;width:379px;height:90px}
  .footer__band{position:absolute;left:0;top:0}
  .phone{position:absolute;left:0;right:0;top:28px;display:flex;align-items:center;justify-content:center;gap:8px;color:#fff;font-family:"Questrial",sans-serif;font-size:38px;line-height:38px;letter-spacing:.5px}
  .phone__icon{flex:none}

  .quote{position:absolute;left:26px;top:213px;width:328px;height:79px;border:1.5px solid var(--red);border-radius:4px;padding:9px 14px 0 14px}
  .quote__mark{position:absolute;font-family:"Lato",sans-serif;font-weight:700;font-size:30px;line-height:14px;height:14px;color:var(--red);background:#fff;padding:0 3px}
  .quote__mark--open{left:8px;top:-7px}
  .quote__mark--close{right:22px;bottom:-7px;line-height:22px;height:14px;overflow:visible}
  .quote__text{font-style:italic;font-size:14px;line-height:18px}
  .quote__by{text-align:right;font-weight:700;font-size:14.5px;margin-top:4px}

  .conditions-head{position:absolute;left:26px;top:317px;width:328px;height:29px;background:var(--grey-bar);color:#fff;font-weight:700;font-size:12.3px;line-height:29px;padding-left:6px;border-radius:3px 3px 0 0;white-space:nowrap}
  .conditions{position:absolute;left:26px;top:346px;width:328px;height:387px;background:var(--list-bg);border-radius:0 0 4px 4px;list-style:none;display:grid;grid-template-columns:155px 173px;grid-auto-flow:column;grid-template-rows:repeat(14,27.2px);font-size:12.3px}
  .conditions li{position:relative;padding-left:16px;line-height:27.2px;white-space:nowrap}
  .conditions li::before{left:7px;top:12px}
  .conditions li:nth-child(n+15){padding-left:11px}
  .conditions li:nth-child(n+15)::before{left:2px}
</style>
</head>
<body>

<section class="rack-card rack-card--front">
  <div class="hero">
    <svg class="hero__rings" width="379" height="500" viewBox="0 0 379 500">
      <path d="M0 455 Q40 428 72 414" stroke="var(--red)" stroke-width="7" fill="none"/>
      <path d="M379 450 Q345 426 310 412" stroke="var(--red)" stroke-width="7" fill="none"/>
      <ellipse cx="191" cy="329" rx="156" ry="155" stroke="var(--red)" stroke-width="4" fill="none"/>
    </svg>
    <div class="hero__photo" role="img" aria-label="Photo of a water bottle standing between two blue dumbbells on a wooden deck"></div>
  </div>
  <div class="brand-mark brand-mark--front">
    <div class="brand-mark__dot"></div>
    <div class="brand-mark__name">BRIGHTPATH<br>MEDICAL EXERCISE</div>
  </div>
  <h1 class="title">BRIGHTPATH<br>MEDICAL EXERCISE, LLC</h1>
  <p class="tagline">“Getting You Back To Function As<br>Quickly And Safely As Possible”</p>
  <div class="label">OUR PRODUCTS AND SERVICES:</div>
  <ul class="services">
    <li>Initial Assessment and Functional Screening</li>
    <li>One-On-One supervised post rehab exercise</li>
    <li>Online consultation with individualized home exercise program</li>
  </ul>
  <footer class="footer">
    <svg class="footer__band" width="379" height="90" viewBox="0 0 379 90"><path d="M0 24 Q190 -6 379 0 L379 90 L0 90 Z" fill="var(--dark)"/></svg>
    <div class="phone">
      <svg class="phone__icon" width="36" height="36" viewBox="0 0 38 38"><circle cx="19" cy="19" r="17" fill="none" stroke="var(--red)" stroke-width="2.5"/><path d="M13 11c1-1 2-1 3 0l2 3c.5 1 0 2-1 2.5-.5.3-.5 1 0 2l2.5 2.5c1 .5 1.7.5 2 0 .5-1 1.5-1.5 2.5-1l3 2c1 1 1 2 0 3-2 2-5 2-9-1.5S11 14 13 11z" fill="var(--red)"/></svg>
      <span>5550142873</span>
    </div>
  </footer>
</section>

<section class="rack-card rack-card--back">
  <div class="brand-mark brand-mark--back">
    <div class="brand-mark__dot"></div>
    <div class="brand-mark__name">BRIGHTPATH<br>MEDICAL EXERCISE</div>
  </div>
  <blockquote class="quote">
    <span class="quote__mark quote__mark--open">“</span>
    <p class="quote__text">Exercise is the key to long-term management of most medical conditions</p>
    <p class="quote__by">- Daniel R Hayes, PhD, PT</p>
    <span class="quote__mark quote__mark--close">”</span>
  </blockquote>
  <div class="conditions-head">We offer management of the following conditions &amp; more:</div>
  <ul class="conditions">
    <li>Diabetes AC</li><li>Hypertension</li><li>ACL Rupture</li><li>Ankle Fracture</li><li>Bicipital Tendonitis</li><li>Total Hip Replacement</li><li>Total Knee Replacement</li><li>Spinal Stenosis</li><li>Multiple Sclerosis</li><li>Shoulder Dislocation</li><li>Scoliosis</li><li>Osteoporosis</li><li>Osteoarthritis</li><li>Cervical disc herniation</li>
    <li>Joint Separation</li><li>Fibromyalgia</li><li>Spondylothesis</li><li>Parkinson’s Disease</li><li>Tibial Plateau Fracture</li><li>Tennis Elbow/Golfer’s Elbow</li><li>Carpal Tunnel Syndrome</li><li>Total Shoulder Replacement</li><li>Bicipital Tendonitis</li><li>Patello-Femoral Syndrome</li><li>Rotator Cuff Syndrome</li><li>Cervical Strain</li><li>Impingement Syndrome</li><li>Laminectomy</li>
  </ul>
  <footer class="footer">
    <svg class="footer__band" width="379" height="90" viewBox="0 0 379 90"><path d="M0 24 Q190 -6 379 0 L379 90 L0 90 Z" fill="var(--dark)"/></svg>
    <div class="phone">
      <svg class="phone__icon" width="36" height="36" viewBox="0 0 38 38"><circle cx="19" cy="19" r="17" fill="none" stroke="var(--red)" stroke-width="2.5"/><path d="M13 11c1-1 2-1 3 0l2 3c.5 1 0 2-1 2.5-.5.3-.5 1 0 2l2.5 2.5c1 .5 1.7.5 2 0 .5-1 1.5-1.5 2.5-1l3 2c1 1 1 2 0 3-2 2-5 2-9-1.5S11 14 13 11z" fill="var(--red)"/></svg>
      <span>5550142873</span>
    </div>
  </footer>
</section>

</body>
</html>
```